MOLVT Study flyer

I need help designing a flyer for a research study that will include brain imaging in adolescents. The info is in the attached document. The study is called the Marrowby Orchard Lantern Vesper Trail (MOLVT) study. Ideally this would be returned as a document that I can edit in the future as we will have several new recruitment phases (different age groups, etc. I also would love to have a logo designed as part of this project, but I recognize that might be a separate design request.

```html
<!DOCTYPE html>
<html lang="en">
<head>
<meta charset="utf-8">
<title>MOLVT Study – Recruitment Flyer</title>
<link href="https://fonts.googleapis.com/css2?family=Figtree:wght@400;500;600;700;800&display=swap" rel="stylesheet">
<style>
  :root {
    --navy: #13245a;
    --navy-deep: #0d1a45;
    --teal: #3fb8b8;
    --teal-dark: #1f8a8a;
    --purple: #6a3d9a;
    --purple-soft: #f1ecf8;
    --teal-soft: #eaf6f6;
    --blue-soft: #ebf0fa;
    --blue: #2756c5;
    --ink: #1a2040;
    --white: #ffffff;
    --gold: #f2c04b;
    --line: #c8d0e0;
  }
  * { box-sizing: border-box; margin: 0; padding: 0; }
  html, body { width: 848px; height: 1200px; overflow: hidden; background: var(--white); }
  body { font-family: "Figtree", Arial, sans-serif; color: var(--ink); }
  .flyer { position: relative; width: 848px; height: 1200px; overflow: hidden; background: var(--white); }

  /* Header */
  .masthead { position: absolute; top: 0; left: 0; width: 848px; height: 150px; }
  .study-mark { position: absolute; left: 56px; top: 32px; }
  .study-name { display: flex; align-items: center; gap: 12px; color: var(--navy); font-weight: 700; font-size: 44px; letter-spacing: 2px; line-height: 1; }
  .study-name .dot { width: 22px; height: 22px; border-radius: 50%; background: var(--teal); }
  .study-label { margin: 8px 0 0 34px; color: var(--teal-dark); font-weight: 600; font-size: 16px; letter-spacing: 6px; }
  .study-full { margin: 8px 0 0 34px; color: var(--purple); font-weight: 500; font-size: 11.5px; line-height: 1.35; width: 200px; }
  .divider { position: absolute; left: 392px; top: 34px; width: 1px; height: 106px; background: var(--line); }
  .uni { position: absolute; left: 434px; top: 44px; }
  .uni-name { display: flex; align-items: center; gap: 10px; color: var(--navy); font-weight: 600; font-size: 24px; line-height: 1.1; }
  .uni-name .square { width: 30px; height: 30px; background: var(--gold); }
  .uni-dept { margin: 10px 0 0 40px; color: var(--navy); font-size: 10.5px; font-weight: 600; letter-spacing: .4px; line-height: 1.4; }
  .uni-dept span { display: block; font-weight: 400; }

  /* Hero */
  .hero-band { position: absolute; left: 0; top: 0; width: 848px; height: 500px; }
  .hero-photo { position: absolute; left: 436px; top: 150px; width: 412px; height: 276px;
    background: linear-gradient(120deg, #b9a9c9 0%, #8f7fa8 40%, #2c3a68 75%, #1a2a55 100%); clip-path: ellipse(110% 100% at 100% 30%); }
  .hero-copy { position: absolute; left: 38px; top: 212px; width: 400px; color: var(--white); }
  .hero-copy .lead { font-size: 33px; font-weight: 700; line-height: 1.15; }
  .hero-copy .age { font-size: 44px; font-weight: 800; color: var(--teal); line-height: 1.15; }
  .hero-copy .rule { width: 240px; height: 3px; background: var(--purple); margin: 10px 0 14px; border-radius: 2px; }
  .hero-copy .question { font-size: 26px; font-weight: 700; line-height: 1.3; }

  /* Intro box */
  .intro { position: absolute; left: 38px; top: 425px; width: 747px; height: 140px; background: var(--white); border: 1px solid var(--line); border-radius: 10px; display: flex; align-items: center; }
  .intro .badge { margin-left: 48px; width: 118px; height: 118px; border-radius: 50%; background: var(--teal-soft); flex: none; }
  .intro p { margin-left: 28px; width: 470px; font-size: 17.5px; font-weight: 600; line-height: 1.5; color: var(--navy); }
  .intro p em { font-style: normal; color: var(--teal-dark); }

  /* Steps */
  .steps-title { position: absolute; left: 38px; top: 580px; width: 747px; display: flex; align-items: center; gap: 14px; color: var(--navy); font-weight: 700; font-size: 20px; }
  .steps-title::before, .steps-title::after { content: ""; flex: 1; height: 2px; background: var(--teal-dark); }
  .step { position: absolute; top: 624px; height: 213px; border-radius: 12px; text-align: center; font-size: 14px; font-weight: 600; line-height: 1.4; color: var(--navy-deep); }
  .step .num { position: absolute; left: 25px; top: 1px; width: 32px; height: 32px; border-radius: 50%; color: var(--white); font-weight: 700; font-size: 17px; line-height: 32px; text-align: center; }
  .step .icon { margin: 12px auto 0; height: 84px; border-radius: 10px; }
  .step p { margin: 14px 12px 0; }
  .step-interview { left: 42px; width: 227px; background: var(--purple-soft); }
  .step-interview .num { background: var(--purple); }
  .step-interview .icon { width: 96px; background: #ddd0ee; }
  .step-survey { left: 285px; width: 184px; background: var(--teal-soft); }
  .step-survey .num { background: var(--teal-dark); left: 18px; }
  .step-survey .icon { width: 64px; background: #cbe9e9; }
  .step-survey p { margin-top: 34px; }
  .step-scan { left: 485px; width: 302px; background: var(--blue-soft); }
  .step-scan .num { background: var(--blue); }
  .step-scan .icon { width: 126px; background: #d4def4; }

  /* Eligibility */
  .eligibility { position: absolute; left: 35px; top: 859px; width: 367px; height: 188px; border: 1.5px solid var(--teal); border-radius: 8px; padding: 14px 22px 0 22px; }
  .eligibility h3 { color: var(--teal-dark); font-size: 19px; font-weight: 700; margin-bottom: 10px; }
  .eligibility ul { list-style: none; }
  .eligibility li { display: flex; align-items: center; gap: 16px; font-size: 13px; line-height: 1.3; padding: 6px 0; border-bottom: 1px dashed var(--line); min-height: 40px; }
  .eligibility li:last-child { border-bottom: none; }
  .eligibility svg { flex: none; }

  .family-photo { position: absolute; left: 402px; top: 865px; width: 274px; height: 190px; border-radius: 0 20px 0 0;
    background: linear-gradient(135deg, #e9dfd6 0%, #c9aa98 45%, #b8a4cc 100%); }
  .brain-art { position: absolute; left: 662px; top: 850px; width: 186px; height: 210px;
    background: radial-gradient(circle at 55% 45%, #3a3e9a 0%, #2a2f78 35%, #9b8ad6 65%, rgba(170,210,230,.6) 85%, rgba(255,255,255,0) 100%); }

  /* Footer */
  .footer { position: absolute; left: 0; top: 1060px; width: 848px; height: 140px; background: var(--navy); }
  .footer .mail { position: absolute; left: 52px; top: 10px; width: 68px; height: 68px; border-radius: 50%; background: var(--white); display: flex; align-items: center; justify-content: center; }
  .footer .ask { position: absolute; left: 135px; top: 14px; color: var(--white); font-size: 22px; font-weight: 500; line-height: 1.3; }
  .footer .rule { position: absolute; left: 135px; top: 75px; width: 385px; height: 2px; background: var(--teal); }
  .footer .email { position: absolute; left: 135px; top: 89px; color: var(--teal); font-size: 24px; font-weight: 600; }
  .payment { position: absolute; left: 586px; top: 1038px; width: 176px; height: 176px; border-radius: 50%; background: var(--gold); border: 3px solid #ffe08e; text-align: center; color: var(--navy); }
  .payment svg { margin-top: 24px; }
  .payment .label { font-size: 15px; font-weight: 600; line-height: 1.2; margin-top: 2px; }
  .payment .amount { font-size: 40px; font-weight: 800; line-height: 1.1; }
</style>
</head>
<body>
<main class="flyer">

  <svg class="hero-band" viewBox="0 0 848 500" aria-hidden="true">
    <defs>
      <linearGradient id="heroBg" x1="0" y1="0" x2="1" y2="1">
        <stop offset="0" stop-color="#1b2f6e"/>
        <stop offset="1" stop-color="#0d1a45"/>
      </linearGradient>
    </defs>
    <path d="M0 146 Q420 170 848 140 L848 500 L0 500 Z" fill="url(#heroBg)"/>
  </svg>

  <header class="masthead">
    <div class="study-mark">
      <div class="study-name"><span class="dot"></span>MOLVT</div>
      <div class="study-label">STUDY</div>
      <div class="study-full">Marrowby Orchard Lantern Vesper Trail</div>
    </div>
    <div class="divider"></div>
    <div class="uni">
      <div class="uni-name"><span class="square"></span>Halbrook University</div>
      <div class="uni-dept">SCHOOL OF MEDICINE<span>DEPARTMENT OF PSYCHIATRY</span></div>
    </div>
  </header>

  <div class="hero-photo" role="img" aria-label="Photo of a thoughtful teenage girl in a lilac hoodie with brain scan images on a monitor behind her"></div>

  <section class="hero-copy">
    <div class="lead">Are you the parent of</div>
    <div class="age">a child age 10-17?</div>
    <div class="rule"></div>
    <div class="question">Do they worry or overthink negative emotions?</div>
  </section>

  <section class="intro">
    <div class="badge" role="img" aria-label="Brain icon"></div>
    <p>Halbrook University researchers are seeking girls <em>age 10-17</em> for a study about brain activity in emotions and decision-making and how they relate to puberty, anxiety and depression.</p>
  </section>

  <h2 class="steps-title">Study participation involves:</h2>

  <article class="step step-interview">
    <span class="num">1</span>
    <div class="icon" role="img" aria-label="Icon of two people talking"></div>
    <p>One one-hour interview (online or in-person) where your child will discuss their thoughts</p>
  </article>
  <article class="step step-survey">
    <span class="num">2</span>
    <div class="icon" role="img" aria-label="Clipboard checklist icon"></div>
    <p>Online questionnaires (parent and child)</p>
  </article>
  <article class="step step-scan">
    <span class="num">3</span>
    <div class="icon" role="img" aria-label="MRI scanner icon"></div>
    <p>One two-hour visit where your child will complete an MRI scan, answer questions about their puberty stage, and have a small hair sample taken to study puberty hormones</p>
  </article>

  <section class="eligibility">
    <h3>Your child may be eligible if they:</h3>
    <ul>
      <li><svg width="32" height="32" viewBox="0 0 32 32"><circle cx="16" cy="16" r="16" fill="#1f8a8a"/><path d="M9 16.5l5 5 9-10" fill="none" stroke="#fff" stroke-width="3" stroke-linecap="round" stroke-linejoin="round"/></svg>Are age 10-17</li>
      <li><svg width="32" height="32" viewBox="0 0 32 32"><circle cx="16" cy="16" r="16" fill="#1f8a8a"/><path d="M9 16.5l5 5 9-10" fill="none" stroke="#fff" stroke-width="3" stroke-linecap="round" stroke-linejoin="round"/></svg>Tend to worry or<br>overthink negative thoughts</li>
      <li><svg width="32" height="32" viewBox="0 0 32 32"><circle cx="16" cy="16" r="16" fill="#1f8a8a"/><path d="M9 16.5l5 5 9-10" fill="none" stroke="#fff" stroke-width="3" stroke-linecap="round" stroke-linejoin="round"/></svg>have not been diagnosed with psychosis, learning problems, or autism</li>
    </ul>
  </section>

  <div class="family-photo" role="img" aria-label="Photo of a mother and teenage daughter talking together"></div>
  <div class="brain-art" role="img" aria-label="Watercolour illustration of a head silhouette with a glowing brain"></div>

  <footer class="footer">
    <div class="mail">
      <svg width="38" height="28" viewBox="0 0 38 28" aria-hidden="true"><rect x="2" y="2" width="34" height="24" rx="3" fill="none" stroke="#1f8a8a" stroke-width="3"/><path d="M3 4l16 12 16-12" fill="none" stroke="#1f8a8a" stroke-width="3" stroke-linejoin="round"/></svg>
    </div>
    <div class="ask">Interested in participating?<br>Want more information?</div>
    <div class="rule"></div>
    <div class="email">molvtstudy@halbrookhealth.edu</div>
  </footer>

  <div class="payment">
    <svg width="38" height="38" viewBox="0 0 38 38" aria-hidden="true"><rect x="4" y="14" width="30" height="21" fill="none" stroke="#13245a" stroke-width="2.5"/><rect x="2" y="9" width="34" height="6" fill="none" stroke="#13245a" stroke-width="2.5"/><path d="M19 9v26M19 9c-3-6-10-7-10-2s7 2 10 2c3 0 10 3 10-2s-7-4-10 2" fill="none" stroke="#13245a" stroke-width="2.5"/></svg>
    <div class="label">Compensation<br>up to</div>
    <div class="amount">$140</div>
  </div>

</main>
</body>
</html>
```